business card for a shoe shop

we would like a business card for a family owned shoe shop.
With this information included.
Darnell's Shoe Store
Family owned since 1947

then on other side
Darnell's Shoe Store
Footwear fitting specialist
Phone: 9187 2630
218 Quarry St, Fernleigh Downs 3187
(cnr. Hartwick Rd and Quarry St)
darnellshoes218@examplemail.com
if could incorporate the purple color on card i have attached.

```html
<!DOCTYPE html>
<html lang="en">
<head>
<meta charset="utf-8">
<title>Darnell's Shoe Store – Business Card</title>
<link href="https://fonts.googleapis.com/css2?family=Poppins:wght@400;500;600&display=swap" rel="stylesheet">
<style>
  :root {
    --purple: #8a3ffb;
    --purple-light: #9f6bfc;
    --purple-deep: #6c28e4;
    --charcoal: #2f2f2f;
    --white: #ffffff;
    --backdrop: #ece9f1;
  }
  * { box-sizing: border-box; margin: 0; padding: 0; }
  html, body {
    width: 1200px;
    height: 1181px;
    overflow: hidden;
    background: var(--backdrop);
    font-family: "Poppins", sans-serif;
    color: var(--white);
  }
  .canvas { position: relative; width: 1200px; height: 1181px; }

  .card {
    position: absolute;
    width: 654px;
    height: 403px;
    overflow: hidden;
    box-shadow: 0 10px 30px rgba(40, 20, 80, 0.18);
  }

  /* Front */
  .card-front { left: 179px; top: 166px; background: var(--purple); }
  .front-top-strip { position: absolute; left: 0; top: 0; width: 100%; height: 17px; background: var(--purple); }
  .front-dark-band { position: absolute; left: 0; top: 17px; width: 100%; height: 147px; background: var(--charcoal); }
  .brand-circle {
    position: absolute;
    left: 245px; top: 8px;
    width: 164px; height: 164px;
    border-radius: 50%;
    background: var(--white);
    border: 10px solid var(--purple);
  }
  .brand-name {
    position: absolute;
    left: 0; top: 188px; width: 100%;
    text-align: center;
    font-weight: 500;
    font-size: 46px;
    line-height: 1;
    letter-spacing: 1px;
  }
  .brand-sub {
    position: absolute;
    left: 0; top: 236px; width: 100%;
    display: flex;
    justify-content: center;
    align-items: center;
    gap: 8px;
    font-weight: 500;
    font-size: 20px;
    line-height: 26px;
    letter-spacing: 4px;
  }
  .brand-sub::before,
  .brand-sub::after {
    content: "";
    width: 58px;
    height: 1.5px;
    background: var(--white);
  }
  .specialty {
    position: absolute;
    left: 0; top: 271px; width: 100%;
    text-align: center;
    font-weight: 600;
    font-size: 23px;
    letter-spacing: -0.3px;
  }
  .contact-list {
    position: absolute;
    left: 37px; top: 330px;
    list-style: none;
    font-size: 16px;
    line-height: 23px;
  }
  .contact-list li { display: flex; align-items: center; gap: 8px; white-space: nowrap; }
  .contact-list svg { width: 15px; height: 15px; flex: none; }
  .address {
    position: absolute;
    right: 51px; top: 318px;
    text-align: right;
    font-style: normal;
    font-size: 14px;
    line-height: 20px;
    white-space: nowrap;
  }

  /* Back */
  .card-back { left: 475px; top: 627px; }
  .back-pattern-area {
    position: absolute; inset: 0;
    background: linear-gradient(180deg, var(--purple-light) 0%, var(--purple) 55%, var(--purple-deep) 100%);
  }
  .back-tagline {
    position: absolute;
    left: 0; top: 342px; width: 100%;
    text-align: center;
    font-size: 20px;
    font-weight: 400;
  }
</style>
</head>
<body>
<main class="canvas">

  <section class="card card-front" aria-label="Business card front">
    <div class="front-top-strip"></div>
    <div class="front-dark-band"></div>
    <div class="brand-circle"></div>
    <h1 class="brand-name">DARNELL'S</h1>
    <p class="brand-sub">SHOE STORE</p>
    <h2 class="specialty">FOOTWEAR FITTING SPECIALIST</h2>

    <ul class="contact-list">
      <li>
        <svg viewBox="0 0 16 16" aria-hidden="true"><path fill="#fff" d="M1 6c0-2 3-3 7-3s7 1 7 3v1h-3V5.6C11 5.3 9.6 5.1 8 5.1S5 5.3 4 5.6V7H1zM4.5 7.5h7L14 13H2z"/></svg>
        <span>9187 2630</span>
      </li>
      <li>
        <svg viewBox="0 0 16 16" aria-hidden="true"><rect x="1" y="3" width="14" height="10" fill="#fff"/><path d="M1.5 3.5 8 9l6.5-5.5M1.5 12.5 6 8m4 0 4.5 4.5" stroke="#8a3ffb" stroke-width="1.2" fill="none"/></svg>
        <span>darnellshoes218@examplemail.com</span>
      </li>
    </ul>

    <address class="address">
      218 Quarry St,<br>
      Fernleigh Downs 3187<br>
      (cnr. Hartwick Rd and Quarry St)
    </address>
  </section>

  <section class="card card-back" aria-label="Business card back">
    <div class="back-pattern-area" role="img" aria-label="Repeating tonal purple pattern of the shop's brand mark"></div>
    <p class="back-tagline">Family owned since 1947</p>
  </section>

</main>
</body>
</html>
```